lotus bowl vietnamese restaurant in need of a new menu

a family owned vietnamese restaurant in need of a new menu design that is fun, classy, and yet simple. menu that will catch the customers eyes. easy to read yet flows nicely. like to use the color green (basil green color) creme yellow and maroon. open to other colors as long as it looks nice together. our restaurant is family oriented, casual yet has a nice ambiance atmosphere.
prefer 11x17 portrait double sided. attached is our menu with the current price updated so use the info on this to start creating! looking for something unique, professional and one of a kind menu!
please use your own creative layout and design. we are open to ideas. the files uploaded are the updated prices and the logo is to use whichever one you feel goes with the menu.
Reason: don't see anything we like so far...please be creative!
Target Market(s)
restaurant consumers
Industry/Entity Type
Restaurant
Look and feel

```html
<!DOCTYPE html>
<html lang="en">
<head>
<meta charset="utf-8">
<title>Lotus Bowl – Take Out Menu</title>
<link rel="stylesheet" href="https://fonts.googleapis.com/css2?family=Didact+Gothic&family=Open+Sans:ital,wght@0,400;0,600;0,700;1,400&family=Roboto+Condensed:wght@400;700&display=swap">
<style>
:root{
  --basil:#6cbb2a;
  --basil-dark:#3f9a1f;
  --basil-light:#9fd45a;
  --creme-yellow:#f2e600;
  --maroon:#8c1b1b;
  --ink:#4a4a4a;
  --paper:#ffffff;
  --mist:#eef0ee;
  --backdrop:#e6e6e6;
}
*{box-sizing:border-box;margin:0;padding:0}
html,body{width:1200px;height:1200px;overflow:hidden;background:var(--backdrop)}
body{position:relative;font-family:"Open Sans",sans-serif;color:var(--ink)}
.spread{position:absolute;left:180px;width:840px;height:546px;background:var(--paper);display:flex;box-shadow:0 4px 14px rgba(0,0,0,.25);overflow:hidden}
.spread--outside{top:36px}
.spread--inside{top:618px}
.panel{position:relative;width:280px;height:100%;overflow:hidden;background:linear-gradient(180deg,#fff 0%,var(--mist) 100%)}
.panel + .panel{border-left:1px solid #e2e2e2}
.swoosh{position:absolute;inset:0;width:100%;height:100%}
.section-head{position:absolute;left:0;right:0;height:14px;display:flex;align-items:center;justify-content:center}
.section-head::before{content:"";position:absolute;left:0;right:0;top:7px;border-top:2px solid #222}
.section-head span{position:relative;background:var(--basil);color:#fff;font-family:"Didact Gothic",sans-serif;font-size:8.5px;letter-spacing:.3px;padding:2px 12px;border-radius:8px;text-transform:uppercase;white-space:nowrap}
.cols{position:absolute;display:flex;gap:12px}
.col{flex:1;display:flex;flex-direction:column;gap:3px}
.item{font-size:5.6px;line-height:1.3}
.row{display:flex;align-items:baseline;gap:1px}
.row .nm{color:var(--basil);white-space:nowrap}
.row i{flex:1;border-bottom:.6px solid #888;margin-bottom:1px}
.row .pr{color:#555}
.ds{font-style:italic;color:#444}
.note{position:absolute;font-size:5.4px;font-style:italic;color:#333;text-align:center}
.photo{position:absolute;border-radius:8px;border:3px solid var(--creme-yellow)}
.disc{position:absolute;border-radius:50%;border:4px solid var(--maroon)}
.warm{background:radial-gradient(circle at 40% 40%,#d99a5a,#8a4a22)}
.fresh{background:radial-gradient(circle at 45% 45%,#a8c86a,#5d7d2c)}
.broth{background:radial-gradient(circle at 45% 45%,#c97d4a,#6e2f18)}
.rice{background:radial-gradient(circle at 45% 45%,#e8c890,#a86a3a)}
.pale{background:radial-gradient(circle at 45% 45%,#f3e6d6,#c8a98c)}
.cool{background:radial-gradient(circle at 45% 45%,#c9bfe0,#7c6a8f)}
.dark{background:radial-gradient(circle at 45% 45%,#7a5a40,#2e1e14)}
.brand-mark{position:absolute;text-align:center;font-family:"Didact Gothic",sans-serif}
.smoothies{position:absolute;left:10px;top:204px;width:260px;font-size:5.6px}
.smoothies .row{margin-bottom:8px}
.flavors{display:grid;grid-template-columns:repeat(3,1fr);font-size:5.4px;color:#222;line-height:1.35}
.fine-print{position:absolute;left:40px;right:12px;bottom:16px;color:#fff;font-size:4.9px;line-height:1.4}
.cover-name{position:absolute;left:0;right:0;top:44px;text-align:center;font-family:"Didact Gothic",sans-serif;font-size:26px;color:#111}
.cover-tag{position:absolute;left:0;right:0;top:86px;text-align:center;font-family:"Didact Gothic",sans-serif;font-size:15px;color:var(--basil-dark)}
.cover-tag b{font-weight:400;color:#111}
.bowl{position:absolute;left:28px;top:110px;width:232px;height:232px;border-radius:50%;border:9px solid #c42020;background:radial-gradient(circle at 50% 45%,#dfe8c4 0%,#8fbf4a 45%,#3f7a1c 80%)}
.cover-title{position:absolute;left:0;right:0;top:418px;text-align:center;font-family:"Roboto Condensed",sans-serif;font-size:26px;color:var(--maroon)}
.cover-title strong{color:var(--creme-yellow);font-weight:700}
.cover-phone{position:absolute;left:0;right:0;top:452px;text-align:center;font-family:"Roboto Condensed",sans-serif;font-weight:700;font-size:28px;color:#fff}
.cover-address{position:absolute;left:22px;right:14px;top:494px;background:#fff;border-radius:9px;text-align:center;font-size:9.5px;font-weight:700;color:var(--maroon);padding:2px 0}
.intro{position:absolute;font-size:5.4px;font-style:italic;text-align:center;color:#333}
.intro em{color:var(--basil);font-style:italic}
.extras{position:absolute;left:8px;top:172px;width:264px;height:54px;border:1px solid #666;border-radius:6px;display:flex;gap:10px;padding:3px 6px;font-size:5.2px;font-style:italic}
.extras .row .nm{color:var(--basil)}
</style>
</head>
<body>

<!-- OUTSIDE SPREAD -->
<section class="spread spread--outside">

  <!-- Vegetarian panel -->
  <article class="panel panel--vegetarian">
    <svg class="swoosh" viewBox="0 0 280 546" preserveAspectRatio="none" aria-hidden="true">
      <path d="M0 170 C90 150 200 250 280 270 L280 546 L0 546Z" fill="var(--creme-yellow)"/>
      <path d="M0 190 C100 180 210 290 280 300 L280 546 L0 546Z" fill="var(--basil)"/>
      <path d="M0 330 C110 300 200 380 280 360 L280 546 L0 546Z" fill="#fff" opacity=".85"/>
    </svg>
    <div class="section-head" style="top:10px"><span>Mon Chay - Vegetarian Plate</span></div>
    <div class="cols" style="left:12px;right:12px;top:38px">
      <div class="col">
        <div class="item"><div class="row"><span class="nm">Goi cuon tofu</span><i></i><span class="pr">4.50</span></div><p class="ds">Fried tofu spring roll</p></div>
        <div class="item"><div class="row"><span class="nm">Soup rau cai (s)</span><i></i><span class="pr">3.00 (l) 5.95</span></div><p class="ds">Vegetables soup</p></div>
        <div class="item"><div class="row"><span class="nm">Pho dau hu rau cai</span><i></i><span class="pr">9.50</span></div><p class="ds">Fried tofu &amp; vegetables noodle soup</p></div>
        <div class="item"><div class="row"><span class="nm">Dau hu xao rau cai</span><i></i><span class="pr">9.95</span></div><p class="ds">Stir fry tofu with mixed vegetables</p></div>
      </div>
      <div class="col">
        <div class="item"><div class="row"><span class="nm">Dau hu xao xa ot</span><i></i><span class="pr">9.95</span></div><p class="ds">Stir fry fried tofu with hot chilli &amp; lemongrass</p></div>
        <div class="item"><div class="row"><span class="nm">Bun xao dau hu rau cai</span><i></i><span class="pr">9.50</span></div><p class="ds">Fried tofu &amp; vegetables fried rice</p></div>
        <div class="item"><div class="row"><span class="nm">Bun dau hu</span><i></i><span class="pr">9.25</span></div><p class="ds">Fried tofu vermicelli bowl</p></div>
      </div>
    </div>
    <div class="photo broth" style="left:24px;top:154px;width:112px;height:88px" role="img" aria-label="Photo of a vegetable noodle soup bowl"></div>
    <div class="photo rice" style="left:150px;top:154px;width:112px;height:88px" role="img" aria-label="Photo of a rice plate with egg"></div>
    <div class="photo warm" style="left:24px;top:254px;width:112px;height:88px" role="img" aria-label="Photo of a glazed fish dish"></div>
    <div class="photo dark" style="left:150px;top:254px;width:112px;height:88px" role="img" aria-label="Photo of stir fried beef with herbs"></div>
    <div class="photo fresh" style="left:24px;top:354px;width:112px;height:88px" role="img" aria-label="Photo of shrimp salad"></div>
    <div class="photo rice" style="left:150px;top:354px;width:112px;height:88px" role="img" aria-label="Photo of fried rice with tomato"></div>
    <div class="photo pale" style="left:24px;top:454px;width:112px;height:82px" role="img" aria-label="Photo of vermicelli noodle bowl"></div>
    <div class="photo warm" style="left:150px;top:454px;width:112px;height:82px" role="img" aria-label="Photo of grilled pork with dipping sauce"></div>
  </article>

  <!-- Beverages panel -->
  <article class="panel panel--beverages">
    <svg class="swoosh" viewBox="0 0 280 546" preserveAspectRatio="none" aria-hidden="true">
      <path d="M0 546 C10 480 90 430 180 420 C230 412 260 380 280 330 L280 546Z" fill="var(--basil)"/>
      <path d="M0 546 C20 500 90 460 170 450 L120 546Z" fill="var(--basil-dark)" opacity=".35"/>
    </svg>
    <div class="section-head" style="top:10px"><span>Beverages</span></div>
    <div class="cols" style="left:10px;right:10px;top:38px">
      <div class="col">
        <div class="item"><div class="row"><span class="nm">Nuoc ngot - soda</span><i></i><span class="pr">1.50</span></div><p class="ds">Kola Bright, diet, zero, Fizzo, Hill Rush, Sunny Pop, Doc Spark, Limetta, ginger ale, root beer</p></div>
        <div class="item"><div class="row"><span class="nm">Nuoc dua</span><i></i><span class="pr">4.25</span></div><p class="ds">Fresh coconut juice</p></div>
        <div class="item"><div class="row"><span class="nm">Cam vat</span><i></i><span class="pr">4.00</span></div><p class="ds">Fresh orange juice</p></div>
        <div class="item"><div class="row"><span class="nm">Da chanh</span><i></i><span class="pr">3.50</span></div><p class="ds">Fresh limeade juice</p></div>
        <div class="item"><div class="row"><span class="nm">Soda da chanh</span><i></i><span class="pr">4.00</span></div><p class="ds">Fresh limeade with club soda</p></div>
        <div class="item"><div class="row"><span class="nm">Thai ice tea</span><i></i><span class="pr">4.00</span></div><p class="ds">Thai tea mix with half &amp; half milk</p></div>
        <div class="item"><div class="row"><span class="nm">Clearbrook sparkling mineral water</span><i></i><span class="pr">1.95</span></div></div>
      </div>
      <div class="col">
        <div class="item"><div class="row"><span class="nm">Cafe sua da or den da</span><i></i><span class="pr">3.50</span></div><p class="ds">Vietnamese milk ice coffee or black coffee (hot or cold)</p></div>
        <div class="item"><div class="row"><span class="nm">Chanh muoi</span><i></i><span class="pr">3.50</span></div><p class="ds">Salty brined lime juice</p></div>
        <div class="item"><div class="row"><span class="nm">Soda chanh muoi</span><i></i><span class="pr">4.25</span></div><p class="ds">Salty brined lime juice with club soda</p></div>
        <div class="item"><div class="row"><span class="nm">Sua hot ga</span><i></i><span class="pr">4.25</span></div><p class="ds">Sweet milk &amp; egg with club soda</p></div>
        <div class="item"><div class="row"><span class="nm">Sau dau nanh</span><i></i><span class="pr">3.00</span></div><p class="ds">Soy bean milk</p></div>
        <div class="item"><div class="row"><span class="nm">Tra da</span><i></i><span class="pr">1.50</span></div><p class="ds">Unsweetened ice tea</p></div>
        <div class="item"><div class="row"><span class="nm">Che 3 mau</span><i></i><span class="pr">3.50</span></div><p class="ds">Vietnamese 3 color dessert</p></div>
      </div>
    </div>
    <div class="smoothies">
      <div class="row" style="width:110px"><span class="nm">SINH TO - PEARL SMOOTHIES</span><i></i><span class="pr">4.50</span></div>
      <div class="flavors"><span>AVOCADO</span><span>BANANA</span><span>COCONUT</span><span>DURIAN</span><span>HONEYDEW</span><span>GREEN TEA</span><span>STRAWBERRY</span><span>TARO</span><span>THAI TEA</span></div>
      <div class="row" style="width:110px;margin-top:10px"><span class="nm">*EXTRA PEARLS</span><i></i><span class="pr">0.75</span></div>
    </div>
    <div class="brand-mark" style="left:0;right:0;top:274px;font-size:19px;line-height:1;color:var(--basil)">LOTUS BOWL</div>
    <div class="disc dark" style="left:2px;top:330px;width:96px;height:96px" role="img" aria-label="Photo of Vietnamese drip coffee"></div>
    <div class="disc fresh" style="left:72px;top:370px;width:80px;height:80px" role="img" aria-label="Photo of three color dessert"></div>
    <div class="disc cool" style="left:164px;top:330px;width:112px;height:112px" role="img" aria-label="Photo of taro pearl smoothie"></div>
    <div class="fine-print">
      <p>* Menu and prices are subject to change without notice. | No substituting food item/s on any entrees.</p>
      <p>** Consuming raw or undercooked meats, poultry, seafood, shellfish, eggs or unpasteurized milk may increase your risk of foodborne illness.</p>
      <p>* Please alert your server for any food allergies/intolerance before ordering.</p>
    </div>
  </article>

  <!-- Cover panel -->
  <article class="panel panel--cover">
    <svg class="swoosh" viewBox="0 0 280 546" preserveAspectRatio="none" aria-hidden="true">
      <path d="M0 410 C60 360 140 330 200 300 C240 280 265 260 280 240 L280 546 L0 546Z" fill="var(--basil)"/>
      <path d="M0 546 L0 470 C80 420 200 400 280 380 L280 546Z" fill="var(--basil-dark)" opacity=".25"/>
    </svg>
    <div class="cover-name">Lotus Bowl</div>
    <div class="cover-tag">Vietnamese <b>Restaurant</b></div>
    <div class="bowl" role="img" aria-label="Photo of a pho bowl topped with herbs, scallions and lime"></div>
    <div class="cover-title">TAKE OUT <strong>MENU</strong></div>
    <div class="cover-phone">(555) 214-0386</div>
    <div class="cover-address">2180 Willow Creek Rd, Fairhaven, FL 33000</div>
  </article>
</section>

<!-- INSIDE SPREAD -->
<section class="spread spread--inside">

  <!-- Appetizers + Hu Tieu -->
  <article class="panel panel--appetizers">
    <svg class="swoosh" viewBox="0 0 280 546" preserveAspectRatio="none" aria-hidden="true">
      <path d="M0 450 C80 420 200 430 280 470 L280 546 L0 546Z" fill="var(--creme-yellow)"/>
    </svg>
    <div class="section-head" style="top:10px"><span>Appetizers</span></div>
    <p class="intro" style="left:10px;right:10px;top:30px">spring rolls (2) comes with lettuce, vermicelli noodles rolled in rice paper served with peanut sauce with choice of: (cannot be mixed):</p>
    <div class="cols" style="left:12px;right:12px;top:52px">
      <div class="col">
        <div class="item"><div class="row"><span class="nm">Goi cuon tom &amp; thit heo</span><i></i><span class="pr">4.50</span></div><p class="ds">shrimp &amp; pork spring rolls</p></div>
        <div class="item"><div class="row"><span class="nm">Goi cuon thit heo / ga / or bo nuong</span><i></i><span class="pr">5.50</span></div><p class="ds">choice of: grilled pork / grilled chicken or grilled beef spring rolls</p></div>
        <div class="item"><div class="row"><span class="nm">Bi cuon</span><i></i><span class="pr">4.50</span></div><p class="ds">pork skin roasted with rice powder spring rolls</p></div>
        <div class="item"><div class="row"><span class="nm">Cha gio (2)</span><i></i><span class="pr">4.50</span></div><p class="ds">fried eggrolls with shrimp, pork &amp; vegetables rolled in egg wrap</p></div>
      </div>
      <div class="col">
        <div class="item"><div class="row"><span class="nm">Canh ga nuoc mam (6)</span><i></i><span class="pr">7.95</span></div><p class="ds">Fried chicken wings</p></div>
        <div class="item"><div class="row"><span class="nm">Gio tom (4)</span><i></i><span class="pr">5.95</span></div><p class="ds">Fried shrimp rolls</p></div>
        <div class="item"><div class="row"><span class="nm">Ca vien chien (8)</span><i></i><span class="pr">4.95</span></div><p class="ds">Fried fish balls</p></div>
        <div class="item"><div class="row"><span class="nm">Chao tom (2)</span><i></i><span class="pr">7.95</span></div><p class="ds">Grilled shrimp paste wrapped around sugar cane stick</p></div>
        <div class="item"><div class="row"><span class="nm">Wonton soup (s)</span><i></i><span class="pr">4.95 (l) 7.50</span></div><p class="ds">Wonton shrimp &amp; pork soup</p></div>
        <div class="item"><div class="row"><span class="nm">Tom cua soup (s)</span><i></i><span class="pr">4.95 (l) 7.50</span></div><p class="ds">Crab meat, shrimp &amp; egg soup</p></div>
      </div>
    </div>
    <p class="intro" style="left:10px;right:10px;top:174px">Vietnamese salad comes with thin cabbage, carrots, onions, mints, crushed peanuts tossed in lime juice &amp; vinegar with the following choices of:</p>
    <div class="cols" style="left:12px;right:12px;top:194px">
      <div class="col">
        <div class="item"><div class="row"><span class="nm">Goi ga - chicken salad</span><i></i><span class="pr">8.95</span></div><p class="ds">shrimp &amp; pork spring rolls</p></div>
        <div class="item"><div class="row"><span class="nm">Bo tai chanh</span><i></i><span class="pr">11.95</span></div><p class="ds">Rare thin sliced beef with onions, mints, basils, crushed peanuts in lime juice &amp; vinegar</p></div>
      </div>
      <div class="col">
        <div class="item"><div class="row"><span class="nm">Goi tom - shrimp salad</span><i></i><span class="pr">9.95</span></div></div>
        <div class="item"><div class="row"><span class="nm">Chim cut roti</span><i></i><span class="pr">11.95</span></div><p class="ds">Roasted quails served with salt &amp; peppered tofu vermicelli bowl</p></div>
      </div>
    </div>
    <div class="section-head" style="top:262px"><span>Hu Tieu (Mi) - Noodle Soup</span></div>
    <p class="intro" style="left:10px;right:10px;top:282px">PORK BROTH WITH RICE OR EGG NOODLE</p>
    <div class="cols" style="left:12px;right:12px;top:294px">
      <div class="col">
        <div class="item"><div class="row"><span class="nm">Hu tieu / mi dac biet</span><i></i><span class="pr">10.50</span></div><p class="ds">Choice of: rice or egg noodle with shrimp, roast pork, chicken, imitation crab, quail eggs, ground pork &amp; fried shrimp cracker combination noodle soup</p></div>
        <div class="item"><div class="row"><span class="nm">Hu tieu / mi hai san</span><i></i><span class="pr">11.50</span></div><p class="ds">Choice of: rice or egg noodle with shrimp, scallops, squid, fish balls &amp; imitation crab noodle soup</p></div>
        <div class="item"><div class="row"><span class="nm">Hu tieu my tho</span><i></i><span class="pr">9.95</span></div><p class="ds">Shrimp, roast pork, chicken, fish ball, imitation crab &amp; ground pork with clear noodle soup</p></div>
        <div class="item"><div class="row"><span class="nm">Hu tieu sate</span><i></i><span class="pr">9.50</span></div><p class="ds">Beef with tomato slices, cucumber, bean sprouts &amp; crushed peanuts in spicy noodle soup</p></div>
      </div>
      <div class="col">
        <div class="item"><div class="row"><span class="nm">Hu tieu / mi kho dac biet</span><i></i><span class="pr">10.95</span></div><p class="ds">Choice of: rice or egg noodle with shrimp, roast pork, chicken, imitation crab, ground pork and fried shrimp cracker with soup on the side</p></div>
        <div class="item"><div class="row"><span class="nm">Mi hoanh thanh</span><i></i><span class="pr">8.95</span></div><p class="ds">Wonton with egg noodle soup</p></div>
        <div class="item"><div class="row"><span class="nm">Xa xiu (roast pork)</span><i></i><span class="pr">9.95</span></div></div>
        <div class="item"><div class="row"><span class="nm">Banh canh tom thit gio heo</span><i></i><span class="pr">9.50</span></div><p class="ds">Shrimp, pork knuckle &amp; vietnamese big noodle soup</p></div>
        <div class="item"><div class="row"><span class="nm">Banh canh ga</span><i></i><span class="pr">8.95</span></div><p class="ds">Chicken with vietnamese big noodle soup</p></div>
      </div>
    </div>
    <div role="img" aria-label="Photo of a shrimp salad with crushed peanuts" style="position:absolute;left:0;right:0;bottom:0;height:90px;background:linear-gradient(180deg,#d8c9a8,#8a9a58);clip-path:polygon(0 25%,40% 8%,100% 30%,100% 100%,0 100%)"></div>
  </article>

  <!-- Pho + Bun -->
  <article class="panel panel--pho">
    <svg class="swoosh" viewBox="0 0 280 546" preserveAspectRatio="none" aria-hidden="true">
      <path d="M0 546 L0 470 C80 430 180 400 280 420 L280 546Z" fill="var(--basil)"/>
      <path d="M0 546 L0 500 C90 460 200 450 280 470 L280 546Z" fill="var(--creme-yellow)"/>
    </svg>
    <div class="section-head" style="top:10px"><span>Pho - Rice Noodle Soup</span></div>
    <div class="cols" style="left:10px;right:10px;top:30px">
      <div class="col">
        <div class="item"><div class="row"><span class="nm">Pho dac biet</span><i></i><span class="pr">9.50</span></div><p class="ds">Steak, brisket, flank, tendon, tripe &amp; meatballs combination noodle soup</p></div>
        <div class="item"><div class="row"><span class="nm">Pho</span><i></i><span class="pr">8.50</span></div><p class="ds">Noodle soup with choices up to 3 items: steak, brisket, flank, tendon, tripe, meatball or vegetables</p></div>
        <div class="item"><div class="row"><span class="nm">Pho ga vietnam (ga di bo)</span><i></i><span class="pr">10.50</span></div><p class="ds">Free range chicken noodle soup</p></div>
        <div class="item"><div class="row"><span class="nm">Pho ga my</span><i></i><span class="pr">9.50</span></div><p class="ds">White chicken &amp; mixed vegetables noodle soup</p></div>
        <div class="item"><div class="row"><span class="nm">Pho thit heo / bo / or ga nuong</span><i></i><span class="pr">10.50</span></div><p class="ds">Choice of: grilled pork, grilled beef or grilled chicken with mixed vegetables</p></div>
      </div>
      <div class="col">
        <div class="item"><div class="row"><span class="nm">Pho do bien</span><i></i><span class="pr">11.50</span></div><p class="ds">Shrimp, scallop, squid, fish balls, imitation crab &amp; vegetables seafood noodle soup</p></div>
        <div class="item"><div class="row"><span class="nm">Pho tom</span><i></i><span class="pr">9.75</span></div><p class="ds">Shrimp with mixed vegetables noodle soup</p></div>
        <div class="item"><div class="row"><span class="nm">Pho do bien chua cay</span><i></i><span class="pr">11.50</span></div><p class="ds">Shrimp, scallop, squid, fish balls &amp; imitation crab in hot &amp; sour noodle soup</p></div>
        <div class="item"><div class="row"><span class="nm">Chao tom (2)</span><i></i><span class="pr">7.95</span></div><p class="ds">Shrimp, scallop, squid, fish balls in hot &amp; sour noodle soup</p></div>
        <div class="item"><div class="row"><span class="nm">Pho tre em</span><i></i><span class="pr">7.25</span></div><p class="ds">Kid's steak &amp; meatball noodle soup</p></div>
      </div>
    </div>
    <div class="extras">
      <div class="col">
        <div class="row"><span class="nm">* x large</span><i></i><span>2.00 more</span></div>
        <div class="row"><span class="nm">* extra meat (steak, chicken, etc.)</span><i></i><span>3.50</span></div>
        <div class="row"><span class="nm">* extra shrimp</span><i></i><span>3.00</span></div>
        <div class="row"><span class="nm">* extra herbs or vegetables</span><i></i><span>1.50</span></div>
        <p style="color:var(--basil)">(ex: onions, cilantros, basils, beansprouts, etc.)</p>
      </div>
      <div class="col">
        <div class="row"><span class="nm">* extra rice, soup or noodles</span><i></i><span>1.50</span></div>
        <div class="row"><span class="nm">* change noodle or brown rice</span><i></i><span>2.00</span></div>
        <div class="row"><span class="nm">* add fried egg</span><i></i><span>1.50</span></div>
        <div class="row"><span class="nm">* add or change to fried rice</span><i></i><span>3.00</span></div>
        <div class="row"><span class="nm">* add eggroll</span><i></i><span>2.25</span></div>
      </div>
    </div>
    <div class="section-head" style="top:236px"><span>Bun - Vermicelli Noodle Bowl</span></div>
    <p class="intro" style="left:10px;right:10px;top:254px">All vermicelli bowl comes with fresh lettuce, bean sprouts, sliced cucumbers, shredded carrots &amp; crushed peanuts</p>
    <div class="cols" style="left:10px;right:10px;top:274px">
      <div class="col">
        <div class="item"><div class="row"><span class="nm">Bun dac biet</span><i></i><span class="pr">12.95</span></div><p class="ds">Choice of: grilled pork, grilled chicken or grilled beef with grilled shrimp &amp; fried eggroll special combination vermicelli bowl</p></div>
        <div class="item"><div class="row"><span class="nm">Bun - vermicelli bowl</span><i></i><span class="pr">8.50</span></div><p class="ds">Choice of: grilled pork, grilled chicken or grilled beef</p></div>
        <div class="item"><div class="row"><span class="nm">+ eggroll</span><i></i><span class="pr">9.95</span></div></div>
        <div class="item"><div class="row"><span class="nm">+ shrimp</span><i></i><span class="pr">10.50</span></div></div>
        <div class="item"><div class="row"><span class="nm">Bun tom nuong (8)</span><i></i><span class="pr">10.95</span></div><p class="ds">Grilled shrimp with vermicelli noodle bowl</p></div>
        <div class="item"><div class="row"><span class="nm">Bun cha gio (3)</span><i></i><span class="pr">9.50</span></div><p class="ds">Fried eggroll vermicelli bowl</p></div>
        <div class="item"><div class="row"><span class="nm">Bun chao tom (2)</span><i></i><span class="pr">9.50</span></div><p class="ds">Grilled shrimp paste vermicelli bowl</p></div>
      </div>
      <div class="col">
        <div class="item"><div class="row"><span class="nm">* 40. Bun bo hue</span><i></i><span class="pr">9.50</span></div><p class="ds">Spicy beef noodle soup with beef shank, pork knuckle, pork blood with large vermicelli noodle</p></div>
        <div class="item"><div class="row"><span class="nm">* 41. Bun rieu</span><i></i><span class="pr">9.50</span></div><p class="ds">Mixed ground pork &amp; crab, pork blood, dried tofu with vermicelli rice noodle in tomato broth soup</p></div>
        <div class="item"><div class="row"><span class="nm">* 42. Bun mang vit</span><i></i><span class="pr">9.50</span></div><p class="ds">Duck &amp; bamboo vermicelli noodle soup</p></div>
      </div>
    </div>
    <div class="disc rice" style="left:30px;top:420px;width:118px;height:118px" role="img" aria-label="Photo of grilled pork vermicelli bowl"></div>
    <div class="disc warm" style="left:146px;top:390px;width:98px;height:98px" role="img" aria-label="Photo of fried spring rolls"></div>
  </article>

  <!-- Com Tam, Com Chien, Xao -->
  <article class="panel panel--rice">
    <svg class="swoosh" viewBox="0 0 280 546" preserveAspectRatio="none" aria-hidden="true">
      <path d="M0 546 L0 400 C80 380 200 420 280 380 L280 546Z" fill="var(--creme-yellow)"/>
      <path d="M0 546 L0 430 C90 410 200 440 280 420 L280 546Z" fill="var(--basil)"/>
    </svg>
    <div class="section-head" style="top:10px"><span>Com Tam - Broken Rice Plate</span></div>
    <div class="cols" style="left:10px;right:10px;top:30px">
      <div class="col">
        <div class="item"><div class="row"><span class="nm">Com dac biet</span><i></i><span class="pr">14.95</span></div><p class="ds">Special rice combination with grilled chicken, grilled pork, grilled shrimp &amp; fried eggroll, crab &amp; egg cake</p></div>
        <div class="item"><div class="row"><span class="nm">Com suon nuong xa</span><i></i><span class="pr">9.95</span></div><p class="ds">Grilled pork chops marinated in lemongrass</p></div>
        <div class="item"><div class="row"><span class="nm">Com suon bi cha</span><i></i><span class="pr">9.50</span></div><p class="ds">Grilled pork chop, pork skin roasted with rice powder &amp; eggcake</p></div>
      </div>
      <div class="col">
        <div class="item"><div class="row"><span class="nm">Com thit nuong, ga nuong or bo nuong</span><i></i><span class="pr">9.75</span></div><p class="ds">Choice of: grilled pork, grilled chicken or grilled beef</p></div>
        <div class="item"><div class="row"><span class="nm">+ shrimp</span><i></i><span class="pr">10.95</span></div><p class="ds">Shrimp with mixed vegetables noodle soup</p></div>
        <div class="item"><div class="row"><span class="nm">Pho do bien chua cay</span><i></i><span class="pr">11.50</span></div></div>
        <div class="item"><div class="row"><span class="nm">Com suon dai han</span><i></i><span class="pr">13.95</span></div><p class="ds">Grilled korean bbq ribs</p></div>
      </div>
    </div>
    <div class="section-head" style="top:114px"><span>Com Chien - Fried Rice</span></div>
    <p class="intro" style="left:10px;right:10px;top:132px">Fried rice is cooked with egg, peas &amp; carrots</p>
    <div class="cols" style="left:10px;right:10px;top:144px">
      <div class="col">
        <div class="item"><div class="row"><span class="nm">Com chien thap cam</span><i></i><span class="pr">10.95</span></div><p class="ds">House special fried rice with shrimp, roasted pork, sausage with peas &amp; carrots</p></div>
        <div class="item"><div class="row"><span class="nm">Com chien tom</span><i></i><span class="pr">9.95</span></div><p class="ds">Shrimp fried rice</p></div>
        <div class="item"><div class="row"><span class="nm">Com chien ga</span><i></i><span class="pr">9.95</span></div><p class="ds">Choice of: chicken fried rice</p></div>
      </div>
      <div class="col">
        <div class="item"><div class="row"><span class="nm">Com chien canh ga</span><i></i><span class="pr">9.50</span></div><p class="ds">Fried rice with fried chicken wings</p></div>
        <div class="item"><div class="row"><span class="nm">Com chien bo luc lac</span><i></i><span class="pr">14.50</span></div><p class="ds">Stir fry (shaking beef) filet mignon with bell peppers with fried rice</p></div>
        <div class="item"><div class="row"><span class="nm">+ shrimps</span><i></i><span class="pr">16.95</span></div><p class="ds">Fried rice is cooked with egg, peas &amp; carrots</p></div>
      </div>
    </div>
    <div class="section-head" style="top:206px"><span>Xao - Stir Fried with Rice Plate</span></div>
    <div class="cols" style="left:10px;right:10px;top:226px">
      <div class="col">
        <div class="item"><div class="row"><span class="nm">Ga xao gung</span><i></i><span class="pr">9.95</span></div><p class="ds">Stir fry chicken with ginger</p></div>
        <div class="item"><div class="row"><span class="nm">Ga or bo xao xa ot</span><i></i><span class="pr">9.95</span></div><p class="ds">Choice of: stir fry chicken or beef in hot chili &amp; lemongrass</p></div>
        <div class="item"><div class="row"><span class="nm">Tom xao xa ot</span><i></i><span class="pr">10.95</span></div><p class="ds">Stir fry shrimp in hot chilli &amp; lemongrass</p></div>
        <div class="item"><div class="row"><span class="nm">Mi xao mem or don hai san</span><i></i><span class="pr">14.95</span></div><p class="ds">Choice of: soft or crispy noodles stir fry with shrimp, squid, fish ball &amp; imitation crab with vegetables</p></div>
      </div>
      <div class="col">
        <div class="item"><div class="row"><span class="nm">Ga or bo xao rau cai</span><i></i><span class="pr">9.95</span></div><p class="ds">Choice of: stir fry chicken or beef with mixed vegetables</p></div>
        <div class="item"><div class="row"><span class="nm">Tom xao rau cai</span><i></i><span class="pr">10.95</span></div><p class="ds">Stir fry shrimp with mixed vegetables</p></div>
        <div class="item"><div class="row"><span class="nm">Tom rang chay mo</span><i></i><span class="pr">10.95</span></div><p class="ds">Stir fry shrimp, ginger, onion &amp; bell pepper in garlic sauce</p></div>
        <div class="item"><div class="row"><span class="nm">* 62. Canh chua ca or tom</span><i></i><span class="pr">14.95</span></div><p class="ds">Choice of: fish or shrimp soup with tomato, pineapple, okra &amp; bean sprouts served with white rice (serving 2-4)</p></div>
        <div class="item"><div class="row"><span class="nm">* 63. Ca kho to</span><i></i><span class="pr">14.95</span></div><p class="ds">Braised swai fish in clay pot with black pepper &amp; dry shallots served with white rice</p></div>
      </div>
    </div>
    <div class="disc pale" style="left:10px;top:362px;width:124px;height:124px" role="img" aria-label="Photo of wonton soup"></div>
    <div class="disc rice" style="left:150px;top:346px;width:124px;height:124px" role="img" aria-label="Photo of house fried rice"></div>
    <div class="disc pale" style="left:66px;top:440px;width:120px;height:120px;background:radial-gradient(circle at 45% 45%,#f5dcd2,#d08f7a)" role="img" aria-label="Photo of fresh shrimp spring rolls"></div>
  </article>
</section>

</body>
</html>
```